Web Design Project for Brightpath Cable Collective

Design a webpage to replace www.brightpathcablecollective.com.au

View the website and design a new website based on the same philosophy of the original.

The website will be fresh, simple, elegant, modern, and a hint of high degree of technical backdrop.

Please utilise the logo in the website design and keep the different contents.

Industry/Entity Type

Group

Requirements
Must have
• Must incorporate the logo which will be uploaded.

```html
<!DOCTYPE html>
<html lang="en">
<head>
<meta charset="utf-8">
<title>Brightpath Cable Collective</title>
<link href="https://fonts.googleapis.com/css2?family=Noto+Sans:wght@400;700&display=swap" rel="stylesheet">
<style>
  :root {
    --brand-blue: #2b3691;
    --ink: #000000;
    --nav-ink: #1a1a1a;
    --paper: #ffffff;
    --stage-dark: #0b0b0b;
    --stage-mid: #4a4a4a;
    --hero-deep: #0d4fa3;
    --hero-light: #d9efff;
  }
  * { margin: 0; padding: 0; box-sizing: border-box; }
  html, body {
    width: 1200px;
    height: 863px;
    overflow: hidden;
    background: var(--paper);
    font-family: "Noto Sans", sans-serif;
    color: var(--ink);
  }
  .site-header {
    position: relative;
    height: 105px;
    background: linear-gradient(180deg, #ffffff 0%, #f4f4f4 100%);
  }
  .brand {
    position: absolute;
    left: 141px;
    top: 12px;
    display: flex;
    align-items: center;
    gap: 12px;
  }
  .brand-mark {
    width: 80px;
    height: 80px;
    border-radius: 50%;
    background: var(--brand-blue);
  }
  .brand-name {
    font-size: 22px;
    font-weight: 700;
    line-height: 1.15;
    color: var(--brand-blue);
    width: 210px;
  }
  .main-nav {
    position: absolute;
    right: 127px;
    top: 77px;
    font-size: 17px;
    color: var(--nav-ink);
    white-space: nowrap;
  }
  .main-nav a { color: inherit; text-decoration: none; }
  .main-nav .sep { margin: 0 4px; }
  .stage {
    height: 512px;
    background: radial-gradient(ellipse 55% 80% at 50% 50%, var(--stage-mid) 0%, #252525 60%, var(--stage-dark) 100%);
    position: relative;
  }
  .hero-visual {
    position: absolute;
    left: 136px;
    top: 39px;
    width: 933px;
    height: 430px;
    border: 1px solid #bbbbbb;
    background: linear-gradient(165deg, var(--hero-light) 0%, #7fc2f0 30%, #2d86d6 55%, var(--hero-deep) 80%, #7fd0f5 100%);
    box-shadow: 0 14px 22px rgba(0,0,0,0.75);
  }
  .content {
    position: relative;
    background: linear-gradient(180deg, #e6e6e6 0%, #ffffff 30px);
    height: 246px;
  }
  .column {
    position: absolute;
    top: 26px;
    width: 285px;
  }
  .column.about { left: 141px; }
  .column.lipsum-one { left: 467px; }
  .column.lipsum-two { left: 792px; }
  .column h2 {
    font-size: 35px;
    font-weight: 400;
    line-height: 1.2;
    margin-bottom: 12px;
  }
  .column p {
    font-size: 14px;
    line-height: 16.3px;
    margin-bottom: 16px;
  }
</style>
</head>
<body>
  <header class="site-header">
    <div class="brand">
      <span class="brand-mark"></span>
      <span class="brand-name">Brightpath Cable Collective</span>
    </div>
    <nav class="main-nav">
      <a href="#">home</a><span class="sep">•</span><a href="#">mission</a><span class="sep">•</span><a href="#">services</a><span class="sep">•</span><a href="#">products</a><span class="sep">•</span><a href="#">partners</a><span class="sep">•</span><a href="#">shop</a><span class="sep">•</span><a href="#">blog</a><span class="sep">•</span><a href="#">contact</a>
    </nav>
  </header>

  <section class="stage">
    <div class="hero-visual" role="img" aria-label="Glowing blue binary digits streaming across a bright light beam"></div>
  </section>

  <main class="content">
    <article class="column about">
      <h2>About Us</h2>
      <p>Brightpath Cable Collective provides products and services through an integrated approach for reliable, mature and flexible solutions.</p>
      <p>Solutions that provide scale from single business premise to multinational offices through-out the world. We understand solutions need to be tailored to your needs; we keep in mind your growth in the years to come.</p>
    </article>
    <article class="column lipsum-one">
      <h2>Lipsum 1</h2>
      <p>Lorem ipsum dolor sit amet, consectetur adipiscing elit. Nulla tincidunt elit vel risus adipiscing eu varius lorem tincidunt. Fusce convallis consectetur neque sed adipiscing. Phasellus nisi justo, semper in condimentum sit amet, auctor id velit. Praesent porta arcu vitae leo euismod tincidunt. Nulla facilisi. In a posuere nunc. Cras ornare ligula sapien. Integer viverra, lacus at convallis porta, mauris felis imperdiet mauris, nec interdum nisi lectus a velit. Donec tincidunt orci.</p>
    </article>
    <article class="column lipsum-two">
      <h2>Lipsum 2</h2>
      <p>Lorem ipsum dolor sit amet, consectetur adipiscing elit. Nulla tincidunt elit vel risus adipiscing eu varius lorem tincidunt. Fusce convallis consectetur neque sed adipiscing. Phasellus nisi justo, semper in condimentum sit amet, auctor id velit. Praesent porta arcu vitae leo euismod tincidunt. Nulla facilisi. In a posuere nunc. Cras ornare ligula sapien. Integer viverra, lacus at convallis porta, mauris felis imperdiet mauris, nec interdum nisi lectus a velit. Donec tincidunt orci.</p>
    </article>
  </main>
</body>
</html>
```